Design mobile friendly real estate and property management company landing page

Design a clean, crisp modern looking landing page that is mobile-friendly (must resize, preferably using bootstrap framework). Landing page will consist of heading with login area, company info, body consists of company description and services, a list of available rental properties with photos, and a footer with additional links and info. Working on updating with text for text areas marked A, B, and C on the layout pdf, but in meantime, lorem ipsum is fine. I can connect events to most buttons, etc. Just need the bootstrap and html functionality set up. Previous company website (which should not be relied upon) is www.qlbt.net This is somewhat of a template for a start, but looking for a more professional and modern design for the new website. But this gives an idea of the content and what needs to be displayed, and how.

Target Market(s)

Clients looking for a property management company that is efficient and well-organized.

Industry/Entity Type

Property Management

Coding

Coded - Design and coding required

Number of Pages Required

1 page

Font styles to use
Sans Serif

Colors
0355a3

Requirements
Must have
• Resize for the screen using bootstrap.
• Navigation that collapses for mobile devices
• Large text boxes and good solid spacing around all elements.
Nice to have
• for property images it would be nice if they can be swiped on touch enabled devices (to the next or previous image). And have navigation that can be clicked to next or previous images.
• Would be nice if a captcha verification was included on contact form.
Should not have
• Fancy or eccentric art

```html
<!DOCTYPE html>
<html lang="en">
<head>
<meta charset="utf-8">
<title>Harborline Realty Services</title>
<link href="https://fonts.googleapis.com/css2?family=Cinzel:wght@400;600;700&family=Lato:ital,wght@0,400;0,700;1,400&display=swap" rel="stylesheet">
<style>
:root{
  --navy:#121b55;
  --navy-dark:#1c2340;
  --ink:#222;
  --muted:#555;
  --nav-bg:#3b4049;
  --nav-dark:#2b2f36;
  --rule:#d6d6d6;
  --cell:#ececec;
  --light:#efefef;
  --footer:#2c2c2c;
  --white:#fff;
}
*{box-sizing:border-box;margin:0;padding:0}
html,body{width:1200px;height:2812px;overflow:hidden}
body{font-family:"Lato",Arial,sans-serif;color:var(--ink);background:var(--white);position:relative}

/* top bar */
.topbar{height:38px;background:var(--navy-dark);color:#fff;font-size:15px;display:flex;align-items:center;padding:0 80px;position:relative}
.topbar .item{display:flex;align-items:center;gap:9px;margin-right:22px}
.topbar .sep{width:1px;height:38px;background:#3e4566;margin-right:22px}
.login{position:absolute;right:80px;top:0;height:38px;width:96px;background:#d4d4d4;color:#222;display:flex;align-items:center;justify-content:center;gap:8px;font-weight:700}

/* header */
.header{height:112px;position:relative}
.brand{position:absolute;left:80px;top:18px;text-align:center;width:352px}
.brand .name{font-family:"Cinzel",Georgia,serif;font-weight:600;font-size:34px;letter-spacing:1px;line-height:42px;color:#111;white-space:nowrap}
.brand .sub{font-family:"Cinzel",Georgia,serif;font-weight:600;font-size:20px;line-height:28px;letter-spacing:8px;color:#111;display:flex;align-items:center;justify-content:center;gap:10px;margin-top:2px}
.brand .sub i{display:block;height:1px;width:70px;background:#333}
.weather{position:absolute;left:774px;top:15px;width:346px;height:82px;background:#f1f1f1;border:1px solid #ddd;padding:6px 8px}
.weather .city{font-size:15px;font-weight:700;color:#333}
.weather .now{display:flex;align-items:center;gap:8px;margin-top:2px}
.weather .temp{font-size:38px;color:#777;line-height:40px}
.weather .today{font-size:12px;color:#444;line-height:14px}
.weather .days{display:flex;gap:12px;margin-left:14px}
.weather .day{font-size:9px;text-align:center;color:#444;width:38px}

/* nav */
.nav{height:45px;background:linear-gradient(#474c55,var(--nav-dark));display:flex;padding:0 80px}
.nav a{font-family:"Cinzel",Georgia,serif;font-weight:600;color:#fff;text-decoration:none;font-size:16px;letter-spacing:1px;height:45px;display:flex;align-items:center;justify-content:center;border-right:1px solid #5b606a}
.nav a:last-child{border-right:none}
.nav a.active{background:#000}

/* hero */
.hero{height:471px;position:relative;background:linear-gradient(180deg,#bcd7ec 0%,#dfeaf2 28%,#3f7fae 46%,#6aa6c5 60%,#c9c3b2 78%,#b4a68c 100%)}
.hero .caption{position:absolute;left:0;right:0;bottom:0;height:73px;background:rgba(40,40,40,.75);padding:0 80px;display:flex;align-items:center;justify-content:space-between}
.hero .caption p{color:#fff;font-size:20px;line-height:24px}
.badges{display:flex;gap:14px;align-items:center}
.badges span{display:block;background:#e8e8e8;border-radius:3px}
.arrow{position:absolute;top:170px;width:48px;height:42px;background:rgba(255,255,255,.75);display:flex;align-items:center;justify-content:center}

/* section titles */
.title{font-family:"Cinzel",Georgia,serif;font-size:34px;line-height:44px;letter-spacing:1px;text-align:center;font-weight:700}
.divider{display:flex;align-items:center;justify-content:center;gap:10px;margin:12px auto 0;width:540px}
.divider i{flex:1;height:1px;background:var(--rule)}

/* welcome */
.welcome{height:296px;padding-top:50px}
.welcome p{width:1040px;margin:24px auto 0;text-align:center;font-size:14px;line-height:24px;color:#222}
.welcome a{color:var(--navy);text-decoration:none}

/* services */
.services{height:418px;background:var(--navy);color:#fff;padding-top:46px;position:relative}
.services .title{color:#fff}
.services .divider i{background:#3a4482}
.service-row{display:flex;justify-content:space-between;width:1080px;margin:48px auto 0}
.service{width:270px;text-align:center}
.service .ring{width:96px;height:96px;border-radius:50%;background:#fff;margin:0 auto;display:flex;align-items:center;justify-content:center}
.service .ring div{width:84px;height:84px;border-radius:50%;background:#3d3d3d;display:flex;align-items:center;justify-content:center}
.service h3{font-family:"Cinzel",Georgia,serif;font-weight:700;font-size:19px;line-height:25px;margin-top:24px;letter-spacing:1px}
.service p{font-size:13px;line-height:18px;margin-top:10px;color:#e6e8f2}
.service .plus{width:16px;height:16px;background:#000;color:#fff;margin:22px auto 0;font-size:14px;line-height:15px;font-weight:700}
.svc-arrow{position:absolute;top:300px;color:#aeb3d0;font-size:30px}

/* properties */
.featured{height:795px;padding-top:52px}
.property{position:absolute;left:80px;width:1040px;height:276px}
.prop-card{position:absolute;left:0;top:0;width:239px;height:276px;border:1px solid #ddd;padding:10px}
.prop-photo{height:140px;position:relative}
.prop-photo .pa{position:absolute;top:58px;width:22px;height:24px;background:rgba(40,40,40,.8);color:#fff;font-size:14px;text-align:center;line-height:24px}
.prop-card h4{font-size:14px;margin-top:10px}
.prop-card p{font-size:13px;line-height:17px;color:#444}
.prop-actions{display:flex;justify-content:space-between;align-items:center;margin-top:12px}
.btn{background:var(--navy);color:#fff;font-size:13px;font-weight:700;width:94px;height:28px;display:flex;align-items:center;justify-content:center}
.detail{font-size:13px;color:#aaa;width:94px;text-align:center;border-bottom:1px solid #ccc;padding-bottom:4px}
.prop-panel{position:absolute;left:267px;top:0;width:773px;height:276px;border:1px solid #ddd}
.prop-head{height:56px;background:var(--navy);color:#fff;display:flex;align-items:center;padding:0 18px;font-family:"Cinzel",Georgia,serif;font-weight:600;font-size:15px;letter-spacing:1px;white-space:nowrap}
.prop-head .addr{display:flex;align-items:center;gap:14px;flex:1}
.prop-head .meta{display:flex;align-items:center;gap:8px;margin-left:18px}
.prop-body{display:flex;height:218px}
.spec{display:grid;grid-template-columns:112px 107px 112px 112px;grid-auto-rows:54.5px}
.spec div{display:flex;align-items:center;font-size:14px;border-bottom:1px solid #e4e4e4}
.spec .k{padding-left:18px;font-weight:700}
.spec .v{background:var(--cell);justify-content:center;border-right:1px solid #e4e4e4}
.spec div:nth-last-child(-n+4){border-bottom:none}
.desc{flex:1;padding:12px 16px;font-size:14px;line-height:20.5px;color:#333}
.desc b{color:var(--navy)}

/* testimonials */
.testimonials{height:300px;background:var(--light);padding-top:46px;position:relative}
.avatar{position:absolute;left:103px;top:149px;width:80px;height:80px;border-radius:50%;border:2px solid var(--navy);background:radial-gradient(circle at 50% 40%,#d9b8a0,#8f8a86)}
.quote{position:absolute;left:220px;top:144px;width:900px;font-style:italic;font-size:13px;line-height:22px;color:#333}
.quote .mk{color:#999;font-size:22px;font-style:normal;font-weight:700}
.t-name{position:absolute;left:220px;top:233px;width:900px;border-top:1px solid #ccc;padding-top:12px;font-weight:700;font-size:15px}
.t-nav{position:absolute;right:80px;top:240px;font-size:20px;font-weight:700;letter-spacing:8px}

/* footer */
.footer{height:291px;background:var(--footer);color:#fff;position:relative}
.fcol{position:absolute;top:26px}
.fcol h5{font-family:"Cinzel",Georgia,serif;font-weight:600;font-size:19px;letter-spacing:1px;padding-bottom:10px;border-bottom:1px solid #444;margin-bottom:14px;white-space:nowrap}
.fcol ul{list-style:none}
.fcol li{font-size:13px;line-height:26.5px}
.fcol li::before{content:"›";margin-right:8px}
.field{width:266px;height:32px;background:#fff;color:#333;font-size:13px;padding:7px 10px;margin-bottom:9px}
.field.msg{height:62px}
.submit{width:88px;height:30px;background:var(--navy);font-family:"Cinzel",Georgia,serif;font-weight:700;font-size:14px;display:flex;align-items:center;justify-content:center;margin-top:12px}
.contact-row{display:flex;gap:14px;margin-bottom:22px;font-size:13px;line-height:18px}
.contact-row .ic{width:30px;height:30px;background:var(--navy);flex:none;display:flex;align-items:center;justify-content:center}
.copyright{height:46px;background:var(--navy);color:#fff;font-size:13px;display:flex;align-items:center;justify-content:center}
</style>
</head>
<body>

<div class="topbar">
  <div class="item"><svg width="16" height="16" viewBox="0 0 24 24"><path fill="#fff" d="M6.6 10.8a15 15 0 0 0 6.6 6.6l2.2-2.2a1 1 0 0 1 1-.25 11.4 11.4 0 0 0 3.6.57 1 1 0 0 1 1 1V20a1 1 0 0 1-1 1A17 17 0 0 1 3 4a1 1 0 0 1 1-1h3.5a1 1 0 0 1 1 1c0 1.25.2 2.45.57 3.57a1 1 0 0 1-.25 1z"/></svg>123-456-7890</div>
  <div class="sep"></div>
  <div class="item"><svg width="16" height="12" viewBox="0 0 16 12"><rect width="16" height="12" fill="#fff"/><path d="M0 0l8 6 8-6" stroke="#1c2340" stroke-width="1.5" fill="none"/></svg>info@harborlinerealty.com</div>
  <div class="login"><svg width="14" height="14" viewBox="0 0 14 14"><path d="M1 7h8M6 4l3 3-3 3M9 1h4v12H9" stroke="#222" stroke-width="1.6" fill="none"/></svg>Login</div>
</div>

<header class="header">
  <div class="brand">
    <div class="name">HARBORLINE REALTY</div>
    <div class="sub"><i></i>SERVICES<i></i></div>
  </div>
  <div class="weather">
    <div class="city">PERTH WEATHER</div>
    <div class="now">
      <svg width="34" height="34" viewBox="0 0 34 34"><circle cx="17" cy="17" r="8" fill="#f5a623"/><g stroke="#f5a623" stroke-width="2"><path d="M17 2v5M17 27v5M2 17h5M27 17h5M6 6l3.5 3.5M24.5 24.5L28 28M6 28l3.5-3.5M24.5 9.5L28 6"/></g></svg>
      <div class="temp">26°C</div>
      <div class="today">Today<br>Cloudy</div>
      <div class="days">
        <div class="day"><svg width="18" height="12"><circle cx="9" cy="6" r="5" fill="#f5a623"/></svg><br>MON<br>18°-20°</div>
        <div class="day"><svg width="18" height="12"><circle cx="9" cy="6" r="5" fill="#f5a623"/></svg><br>TUE<br>28°-30°</div>
        <div class="day"><svg width="18" height="12"><ellipse cx="9" cy="7" rx="8" ry="4" fill="#8cb8d8"/></svg><br>WED<br>20°-23°</div>
        <div class="day"><svg width="18" height="12"><ellipse cx="9" cy="7" rx="8" ry="4" fill="#8cb8d8"/></svg><br>THU<br>26°-31°</div>
      </div>
    </div>
  </div>
</header>

<nav class="nav">
  <a class="active" style="width:104px">HOME</a>
  <a style="width:154px">ABOUT US</a>
  <a style="width:148px">SERVICES</a>
  <a style="width:136px">FOR SALE</a>
  <a style="width:150px">FOR RENT</a>
  <a style="width:178px">TESTIMONIALS</a>
  <a style="width:170px">CONTACT US</a>
</nav>

<section class="hero" role="img" aria-label="Photo of a long wooden pier stretching over the ocean under a blue sky, with waves on the sandy beach">
  <div class="arrow" style="left:0"><svg width="14" height="22"><path d="M12 2L3 11l9 9" stroke="#1c2340" stroke-width="3" fill="none"/></svg></div>
  <div class="arrow" style="right:0"><svg width="14" height="22"><path d="M2 2l9 9-9 9" stroke="#1c2340" stroke-width="3" fill="none"/></svg></div>
  <div class="caption">
    <p>Harborline Realty Services Is A Local, Veteran-owned Small Business Providing<br>Residential Property Management Services Throughout San Diego County</p>
    <div class="badges">
      <span style="width:62px;height:40px;background:#1d4f8c"></span>
      <span style="width:132px;height:40px;background:#6d7f95"></span>
      <span style="width:46px;height:40px"></span>
    </div>
  </div>
</section>

<section class="welcome">
  <h2 class="title">WELCOME TO HARBORLINE REALTY SERVICES</h2>
  <div class="divider"><i></i><svg width="20" height="20" viewBox="0 0 20 20"><path d="M2 10L10 3l8 7v8H2z" fill="#cfcfcf"/></svg><i></i></div>
  <p>Lorem ipsum dolor sit amet, consectetuer adipiscing elit, sed diam nonummy nibh euismod tincidunt ut laoreet dolore magna aliquam erat volutpat. Ut wisi enim ad minim veniam, quis nostrud exerci tation ullamcorper suscipit lobortis nisl ut aliquip ex ea commodo consequat. Duis autem vel eum iriure dolor in hendrerit in vulputate velit esse molestie consequat, vel illum dolore eu feugiat nulla facilisis at vero eros et accumsan et iusto odio dignissim qui blandit praesent luptatum zzril delenit augue duis dolore te feugait nulla facilisi. <a>Read More..</a></p>
</section>

<section class="services">
  <h2 class="title">OUR SERVICES</h2>
  <div class="divider"><i></i><svg width="20" height="20" viewBox="0 0 20 20"><path d="M2 10L10 3l8 7v8H2z" fill="#8a90b8"/></svg><i></i></div>
  <div class="svc-arrow" style="left:52px">‹</div>
  <div class="svc-arrow" style="right:52px">›</div>
  <div class="service-row">
    <div class="service">
      <div class="ring"><div><svg width="40" height="40" viewBox="0 0 40 40"><rect x="8" y="6" width="24" height="30" fill="#fff"/><g fill="#3d3d3d"><rect x="12" y="10" width="4" height="4"/><rect x="18" y="10" width="4" height="4"/><rect x="24" y="10" width="4" height="4"/><rect x="12" y="17" width="4" height="4"/><rect x="18" y="17" width="4" height="4"/><rect x="24" y="17" width="4" height="4"/><rect x="12" y="24" width="4" height="4"/><rect x="24" y="24" width="4" height="4"/><rect x="18" y="28" width="4" height="8"/></g></svg></div></div>
      <h3>APARTMENT<br>MANAGEMENT</h3>
      <p>Lorem ipsum dolor sit amet sect<br>etmo adipiscing elit sed Lore</p>
      <div class="plus">+</div>
    </div>
    <div class="service">
      <div class="ring"><div><svg width="40" height="40" viewBox="0 0 40 40"><path d="M4 20L20 6l16 14" stroke="#fff" stroke-width="3" fill="none"/><path d="M9 18v16h22V18L20 9z" fill="#fff"/><rect x="17" y="24" width="6" height="10" fill="#3d3d3d"/></svg></div></div>
      <h3>FORECLOSURE<br>MANAGEMENT</h3>
      <p>Lorem ipsum dolor sit amet sect<br>etmo adipiscing elit sed Lore</p>
      <div class="plus">+</div>
    </div>
    <div class="service">
      <div class="ring"><div><svg width="40" height="40" viewBox="0 0 40 40"><path d="M4 22L20 8l16 14z" fill="#fff"/><rect x="9" y="22" width="22" height="12" fill="#fff"/><rect x="14" y="25" width="12" height="5" fill="#3d3d3d"/></svg></div></div>
      <h3>HOMEOWNER<br>ASSOCIATION</h3>
      <p>Lorem ipsum dolor sit amet sect<br>etmo adipiscing elit sed Lore</p>
      <div class="plus">+</div>
    </div>
    <div class="service">
      <div class="ring"><div><svg width="40" height="40" viewBox="0 0 40 40"><path d="M20 5L4 19h4v16h24V19h4z" fill="#fff"/><path d="M20 12L11 20v12h18V20z" fill="#3d3d3d"/><rect x="17" y="23" width="6" height="9" fill="#fff"/></svg></div></div>
      <h3>CONDOMINIUM<br>MANAGEMENT</h3>
      <p>Lorem ipsum dolor sit amet sect<br>etmo adipiscing elit sed Lore</p>
      <div class="plus">+</div>
    </div>
  </div>
</section>

<section class="featured">
  <h2 class="title">FEATURED PROPERTIES</h2>
  <div class="divider"><i></i><svg width="20" height="20" viewBox="0 0 20 20"><path d="M2 10L10 3l8 7v8H2z" fill="#cfcfcf"/></svg><i></i></div>

  <article class="property" style="top:1534px">
    <div class="prop-card">
      <div class="prop-photo" role="img" aria-label="Photo of a two-storey pale blue house with white trim and a green lawn" style="background:linear-gradient(180deg,#c9dcec 0%,#b7c4cf 40%,#8fa0ad 65%,#6f8f4a 85%,#5a7a3a 100%)">
        <div class="pa" style="left:0">‹</div><div class="pa" style="right:0">›</div>
      </div>
      <h4>Lorem Ipsum Sit  Dollar Amet</h4>
      <p>Lorem ipsum dolor sit amet, cons ectetur adipiscing elit</p>
      <div class="prop-actions"><div class="btn">For Rent</div><div class="detail">View Detail</div></div>
    </div>
    <div class="prop-panel">
      <div class="prop-head">
        <div class="addr"><svg width="14" height="20" viewBox="0 0 14 20"><path d="M7 0a7 7 0 0 0-7 7c0 5 7 13 7 13s7-8 7-13a7 7 0 0 0-7-7zm0 10a3 3 0 1 1 0-6 3 3 0 0 1 0 6z" fill="#fff"/></svg>LOREM IPSUM SIT  DOLLAR AMET - 12345</div>
        <div class="meta"><svg width="22" height="14" viewBox="0 0 22 14"><path d="M1 0v14M1 10h20v4M1 6h20v4" stroke="#fff" stroke-width="2" fill="none"/></svg>2 BEDROOM</div>
        <div class="meta"><svg width="16" height="18" viewBox="0 0 16 18"><path d="M3 1h10M8 1v6M2 8h12l-2 9H4z" stroke="#fff" stroke-width="2" fill="none"/></svg>1 BATH CONDO</div>
      </div>
      <div class="prop-body">
        <div class="spec">
          <div class="k">Rent</div><div class="v">$ 250.00</div><div class="k">Community</div><div class="v">North Park</div>
          <div class="k">Available</div><div class="v">20 May 2016</div><div class="k">Parking</div><div class="v">136 Sqft</div>
          <div class="k">Sqft</div><div class="v">800 Sqft</div><div class="k">Pets</div><div class="v">Inquire</div>
          <div class="k">Lease</div><div class="v">12 Months</div><div class="k">Laundry</div><div class="v">On Site</div>
        </div>
        <div class="desc"><b>Description:</b> Lorem ipsum dolor sit amet, consectetur adipiscing elit. Sed vitae magna tellus. Aenean ante nunc, semper nec cursus non, rutrum ac eros. Vestibulum mattis justo ac dui bibendum consequat a ac ipsum. Praesent a arcu venenatis, auctor velit eu, suscipit libero. Quisque convallis, leo ac pharetra cursus, ipsum auctor urna, sit amet cursus risus augue in eros...</div>
      </div>
    </div>
  </article>

  <article class="property" style="top:1843px">
    <div class="prop-card">
      <div class="prop-photo" role="img" aria-label="Photo of a grey craftsman-style house with white gables and a front porch" style="background:linear-gradient(180deg,#d5dde4 0%,#9a9fa5 35%,#6d7177 65%,#7c8a6a 88%,#5f6e4a 100%)">
        <div class="pa" style="left:0">‹</div><div class="pa" style="right:0">›</div>
      </div>
      <h4>Lorem Ipsum Sit  Dollar Amet</h4>
      <p>Lorem ipsum dolor sit amet, cons ectetur adipiscing elit</p>
      <div class="prop-actions"><div class="btn">For Sale</div><div class="detail">View Detail</div></div>
    </div>
    <div class="prop-panel">
      <div class="prop-head">
        <div class="addr"><svg width="14" height="20" viewBox="0 0 14 20"><path d="M7 0a7 7 0 0 0-7 7c0 5 7 13 7 13s7-8 7-13a7 7 0 0 0-7-7zm0 10a3 3 0 1 1 0-6 3 3 0 0 1 0 6z" fill="#fff"/></svg>LOREM IPSUM SIT  DOLLAR AMET - 12345</div>
        <div class="meta"><svg width="22" height="14" viewBox="0 0 22 14"><path d="M1 0v14M1 10h20v4M1 6h20v4" stroke="#fff" stroke-width="2" fill="none"/></svg>2 BEDROOM</div>
        <div class="meta"><svg width="16" height="18" viewBox="0 0 16 18"><path d="M3 1h10M8 1v6M2 8h12l-2 9H4z" stroke="#fff" stroke-width="2" fill="none"/></svg>1 BATH CONDO</div>
      </div>
      <div class="prop-body">
        <div class="spec">
          <div class="k">Price</div><div class="v">$ 250.00</div><div class="k">Community</div><div class="v">North Park</div>
          <div class="k">Available</div><div class="v">20 May 2016</div><div class="k">Parking</div><div class="v">136 Sqft</div>
          <div class="k">Sqft</div><div class="v">800 Sqft</div><div class="k">Pets</div><div class="v">Inquire</div>
          <div class="k">Lease</div><div class="v">12 Months</div><div class="k">Laundry</div><div class="v">On Site</div>
        </div>
        <div class="desc"><b>Description:</b> Lorem ipsum dolor sit amet, consectetur adipiscing elit. Sed vitae magna tellus. Aenean ante nunc, semper nec cursus non, rutrum ac eros. Vestibulum mattis justo ac dui bibendum consequat a ac ipsum. Praesent a arcu venenatis, auctor velit eu, suscipit libero. Quisque convallis, leo ac pharetra cursus, ipsum auctor urna, sit amet cursus risus augue in eros...</div>
      </div>
    </div>
  </article>
</section>

<section class="testimonials">
  <h2 class="title">CLIENT  TESTIMONIALS</h2>
  <div class="divider"><i></i><svg width="20" height="20" viewBox="0 0 20 20"><path d="M2 10L10 3l8 7v8H2z" fill="#cfcfcf"/></svg><i></i></div>
  <div class="avatar" role="img" aria-label="Portrait photo of the client"></div>
  <p class="quote"><span class="mk">“</span> Lorem ipsdolor sit amet, consectetur adipiscing elit. Donec sit amet nulla vitae tortor iaculis commodo. Nulla interdum dui vitae lectus malesuada ac dignissim mi vehicula. Nullam ornare vulputate sem vitae convallis. Proin et faucibus eros. Nam id rutrum risus, quis eleifend tortor. Nulla scelerisque vitae ante vitae rhoncus pellentesque turpis. Donec feugiat malesuada justo, quis porta urna egestas nec. Duis nec lobortis justo, ac varius ante. <span class="mk">”</span></p>
  <div class="t-name">Mr. Daren Holt</div>
  <div class="t-nav">‹›</div>
</section>

<footer class="footer">
  <div class="fcol" style="left:80px;width:160px">
    <h5>NAVIGATION</h5>
    <ul><li>Home</li><li>About Us</li><li>Services</li><li>For Sale</li><li>For Rent</li><li>Testimonials</li><li>Contact Us</li></ul>
  </div>
  <div class="fcol" style="left:309px;width:190px">
    <h5>OTHER LINKS</h5>
    <ul><li>Loren ipsum dolor</li><li>Dapibus eget  eleme</li><li>Utm tellus dolor</li><li>Velmki cursu itas</li><li>Fir mnbvcd sirdcnc</li></ul>
  </div>
  <div class="fcol" style="left:544px;width:266px">
    <h5>QUICK CONTACT</h5>
    <div class="field">Name</div>
    <div class="field">Email</div>
    <div class="field msg">Your message</div>
    <div class="submit">SUBMIT</div>
  </div>
  <div class="fcol" style="left:874px;width:246px">
    <h5>GET IN TOUCH</h5>
    <div class="contact-row"><div class="ic"><svg width="12" height="16" viewBox="0 0 14 20"><path d="M7 0a7 7 0 0 0-7 7c0 5 7 13 7 13s7-8 7-13a7 7 0 0 0-7-7zm0 10a3 3 0 1 1 0-6 3 3 0 0 1 0 6z" fill="#fff"/></svg></div><div><b>Harborline Realty Services</b><br>1234 Lren Ipsum dolor suit<br>Nbcdere, IL  1234</div></div>
    <div class="contact-row" style="align-items:center"><div class="ic"><svg width="14" height="14" viewBox="0 0 24 24"><path fill="#fff" d="M6.6 10.8a15 15 0 0 0 6.6 6.6l2.2-2.2a1 1 0 0 1 1-.25 11.4 11.4 0 0 0 3.6.57 1 1 0 0 1 1 1V20a1 1 0 0 1-1 1A17 17 0 0 1 3 4a1 1 0 0 1 1-1h3.5a1 1 0 0 1 1 1c0 1.25.2 2.45.57 3.57a1 1 0 0 1-.25 1z"/></svg></div>123-456-7890</div>
    <div class="contact-row" style="align-items:center"><div class="ic"><svg width="14" height="10" viewBox="0 0 16 12"><rect width="16" height="12" fill="#fff"/><path d="M0 0l8 6 8-6" stroke="#121b55" stroke-width="1.5" fill="none"/></svg></div>info@harborlinerealty.com</div>
  </div>
</footer>
<div class="copyright">Copyright © 2016 Harborline Realty Services  |  All Rights Reserved.</div>

</body>
</html>
```